Tarvin Letterhead Facelift

We need to update our corporate letterhead with a fresh layout. The logo design itself is firm - need fresh layout for the letterhead.

Letter Head Update:

Objective – to update the standard Tarvin letter head so that is more current (2006 was 8 years ago!).

Top header:

1. Delete 1956 and 2006. Put “Est. 1956” on right side of Tarvin logo.

2. Delete “Celebrating 50 years in business”. Replace with “Quality * Capability * Experience”. Use bullet points to separate words.

Bottom header:

1. On bottom page, delete 2006 Venture Prize winner logo. Move the NRQ logo to the right side.

Create a second page and above design (does not put address on the bottom – only keep the logo on the top).

Best design wins! Thank you.

Reminder - deadline for submission is Friday, July 18. Thank you.

```html
<!DOCTYPE html>
<html lang="en">
<head>
<meta charset="utf-8">
<title>Tarvin Industries Letterhead</title>
<link href="https://fonts.googleapis.com/css2?family=Poppins:wght@300;600&display=swap" rel="stylesheet">
<style>
  :root {
    --brand-blue: #1f4a7a;
    --ink-grey: #5a5f66;
    --badge-grey: #8a8d90;
    --paper: #ffffff;
    --backdrop: #e4e5e7;
  }
  * { margin: 0; padding: 0; box-sizing: border-box; }
  html, body {
    width: 1200px;
    height: 968px;
    overflow: hidden;
    background: var(--backdrop);
    font-family: "Poppins", Arial, sans-serif;
  }
  .letterhead {
    position: absolute;
    left: 260px;
    top: 44px;
    width: 680px;
    height: 880px;
    background: var(--paper);
    overflow: hidden;
  }
  .masthead {
    position: absolute;
    top: 54px;
    left: 0;
    width: 100%;
    text-align: center;
    color: var(--brand-blue);
  }
  .wordmark {
    font-weight: 600;
    font-size: 50px;
    line-height: 1;
    letter-spacing: -1px;
  }
  .company-line {
    margin-top: 6px;
    font-weight: 600;
    font-size: 11px;
    letter-spacing: 0.6px;
    text-transform: uppercase;
  }
  .tagline {
    margin-top: 3px;
    font-weight: 300;
    font-size: 10.5px;
    letter-spacing: 1.4px;
    text-transform: uppercase;
  }
  .edge-swoosh {
    position: absolute;
    right: 0;
    top: 360px;
    width: 40px;
    height: 470px;
  }
  .footer {
    position: absolute;
    left: 70px;
    bottom: 46px;
    display: flex;
    align-items: flex-start;
    gap: 14px;
    color: var(--ink-grey);
    font-size: 10px;
    line-height: 1.7;
  }
  .cert-badge {
    width: 22px;
    height: 38px;
    background: var(--badge-grey);
    margin-top: 2px;
  }
  .footer-name {
    color: var(--brand-blue);
    font-weight: 600;
    text-transform: uppercase;
    letter-spacing: 0.4px;
  }
  .contact-row { display: flex; gap: 16px; }
  .contact-item { display: flex; align-items: center; gap: 5px; }
  .contact-item svg { width: 10px; height: 10px; }
</style>
</head>
<body>
  <main class="letterhead">
    <header class="masthead">
      <div class="wordmark">tarvin</div>
      <div class="company-line">Tarvin Industries Ltd. · Est. 1956</div>
      <div class="tagline">Quality · Capability · Experience</div>
    </header>

    <svg class="edge-swoosh" viewBox="0 0 40 470" aria-hidden="true">
      <path d="M40 0 C14 120 6 330 40 470 L40 470 C26 330 28 130 40 0 Z" fill="var(--brand-blue)"/>
      <path d="M40 0 C16 140 4 320 40 470 L40 0 Z" fill="var(--brand-blue)"/>
    </svg>

    <footer class="footer">
      <div class="cert-badge" aria-hidden="true"></div>
      <div class="footer-text">
        <div class="footer-name">Tarvin Industries Ltd.</div>
        <div class="footer-address">4120 Harbourline Road, Delmont, Ontario, Canada, K2P 5R8</div>
        <div class="contact-row">
          <span class="contact-item">
            <svg viewBox="0 0 10 10" aria-hidden="true"><circle cx="5" cy="5" r="5" fill="var(--brand-blue)"/><path d="M3.3 2.6 L4.3 3.6 L3.8 4.3 Q4.6 5.6 5.7 6.2 L6.4 5.7 L7.4 6.7 L6.6 7.5 Q3.4 6.8 2.5 3.4 Z" fill="#fff"/></svg>
            555.014.2287
          </span>
          <span class="contact-item">
            <svg viewBox="0 0 10 10" aria-hidden="true"><circle cx="5" cy="5" r="5" fill="var(--brand-blue)"/><rect x="2.6" y="3.6" width="4.8" height="3" fill="#fff"/><rect x="3.4" y="2.4" width="3.2" height="1.4" fill="#fff"/></svg>
            555.014.2290
          </span>
          <span class="contact-item">
            <svg viewBox="0 0 10 10" aria-hidden="true"><circle cx="5" cy="5" r="4.4" fill="none" stroke="var(--brand-blue)" stroke-width="1.2"/><ellipse cx="5" cy="5" rx="1.8" ry="4.4" fill="none" stroke="var(--brand-blue)" stroke-width="0.8"/><line x1="0.6" y1="5" x2="9.4" y2="5" stroke="var(--brand-blue)" stroke-width="0.8"/></svg>
            www.tarvinindustries.com
          </span>
        </div>
      </div>
    </footer>
  </main>
</body>
</html>
```